High profile consultancy

We need a web design for a company called BK Services. BK as abbreviation for Bold Keystone.

Company focusses on Sourcing (BK Sourcing, focus on ICT), Metrics (BK Metrics; focus on business case analysis and trends in ICT) and Software (BK software; to be developed later on; mainly tools supporting BK soucing and metrics)

Customers base consists of large enterprises, >1000 employees.

Site needs to have menu's for
- services
- login
- about
and a special area ' inspire ' to be able to communicate topics that should inspire our customers to contact us.

but key; it schould communicate our expertise and focus on deep knowlegde of ICT sourcing

Reason: please advice on content management systems to be used to maintain site also please advice on Trovix search clickbids. Will provide feedback on designs shortly.

Target Market(s)

CIO's; board of directors;
company excels in ICT / business knowledge and ability to execute; creates / optimizes relations between ICT suppliers and enterprises.

Requirements
Must have
• website should be easily be found; adaptive by design; accessible by all browsers.
• Need to have a login section for later use
Nice to have
• usage of (draft) logo. see upload.

```html
<!DOCTYPE html>
<html lang="en">
<head>
<meta charset="utf-8">
<title>BK Services</title>
<link href="https://fonts.googleapis.com/css2?family=Arimo:ital,wght@0,400;0,700;1,400&display=swap" rel="stylesheet">
<style>
:root{
  --blue:#1d5d9c;
  --blue-dark:#0f4a86;
  --blue-btn:#2a6fbb;
  --nav-grey:#5d6166;
  --nav-grey-light:#7b7f84;
  --text:#444;
  --muted:#666;
  --line:#e2e2e2;
  --icon-grey:#8a8a8a;
  --social:#d6d6d6;
}
*{box-sizing:border-box;margin:0;padding:0}
html,body{width:1093px;height:1200px;overflow:hidden;background:#fff}
body{font-family:"Arimo",Arial,sans-serif;color:var(--text);position:relative}
.page{position:absolute;left:164px;top:0;width:765px;height:1200px;border-left:1px solid #eee;border-right:1px solid #eee;box-shadow:0 0 6px rgba(0,0,0,.05)}
.abs{position:absolute}
.brand{left:178px;top:30px;display:flex;align-items:center;gap:10px}
.brand-dot{width:34px;height:34px;border-radius:50%;background:var(--blue)}
.brand-name{font-size:30px;color:#555;font-weight:400;letter-spacing:-.5px}
.login-title{left:573px;top:22px;font-size:13px;color:var(--blue)}
.field{top:46px;width:134px;height:20px;border:1px solid #bbb;font-size:8.5px;color:#888;padding:5px 9px;background:#fff}
.btn-login{left:865px;top:46px;width:56px;height:20px;background:linear-gradient(#3c86d4,#1f62ad);color:#fff;font-size:9px;text-align:center;line-height:20px;border-radius:2px}
.login-meta{top:78px;font-size:8px;color:#888}
.check{display:inline-block;width:9px;height:9px;border:1px solid #bbb;vertical-align:-1px;margin-right:6px}
.nav{left:168px;top:108px;width:757px;height:34px;display:flex;background:linear-gradient(var(--nav-grey-light),var(--nav-grey))}
.nav a{color:#fff;text-decoration:none;font-size:10px;display:flex;align-items:center;justify-content:center;border-right:1px solid #888}
.nav a:last-child{border-right:0}
.nav a.active{background:linear-gradient(#4a94e0,#2a6fbb)}
.hero{left:168px;top:141px;width:757px;height:389px;background:linear-gradient(110deg,#4a4c52 0%,#5e6a80 35%,#6f8fbf 60%,#8aa6cc 80%,#7c8698 100%)}
.hero-title{left:202px;top:398px;font-size:29px;color:#fff}
.hero-text{left:203px;top:438px;width:420px;font-size:11.4px;font-style:italic;color:#fff;line-height:20.4px}
.hero-arrow{top:502px;width:21px;height:20px;background:rgba(90,90,90,.6);display:flex;align-items:center;justify-content:center}
.feature{top:554px;width:240px}
.feature-icon{position:absolute;left:0;top:1px;width:38px;height:38px;border-radius:50%;background:var(--icon-grey);display:flex;align-items:center;justify-content:center}
.feature h3{position:absolute;left:50px;top:9px;font-size:13px;font-weight:400;color:var(--blue)}
.feature p{position:absolute;left:51px;top:30px;width:185px;font-size:8.4px;line-height:16.5px;color:var(--text)}
.section-title{font-size:13px;color:var(--blue)}
.testi{left:180px;top:693px;width:734px;height:107px;border:1px solid #eee;border-bottom:0;background:linear-gradient(#f7f7f7,#fff)}
.testi h4{position:absolute;left:49px;top:27px;font-size:10px;font-weight:400;color:var(--blue-dark)}
.testi p{position:absolute;left:49px;top:43px;width:650px;font-size:8.4px;line-height:17px}
.testi .author{position:absolute;left:48px;top:88px;font-size:10px;font-style:italic;color:var(--blue-dark)}
.quote{font-size:30px;color:#c8c8c8;font-family:Georgia,serif}
.update{top:864px;width:169px}
.update .thumb{width:169px;height:92px}
.update h3{margin-top:10px;font-size:13px;font-weight:400;color:var(--blue)}
.update p{margin-top:4px;font-size:8.4px;line-height:16.5px;width:172px}
.update .more{margin-top:9px;width:73px;height:21px;background:linear-gradient(#3b84d2,#1c5ea8);color:#fff;font-size:8.5px;text-align:center;line-height:21px;border-radius:2px}
.rule{left:168px;top:1113px;width:757px;height:3px;background:#ddd}
.foot-links{left:176px;top:1136px;font-size:8px;color:#555;word-spacing:1px}
.foot-links span{margin:0 10px;color:#777}
.copy{left:175px;top:1158px;font-size:7.8px;color:#555}
.socials{left:788px;top:1142px;display:flex;gap:4px}
.socials i{width:19px;height:19px;border-radius:50%;background:var(--social);display:block}
</style>
</head>
<body>
<div class="page"></div>

<header>
  <div class="abs brand"><span class="brand-dot"></span><span class="brand-name">BK Services</span></div>
  <div class="abs login-title">Login</div>
  <div class="abs field" style="left:573px">User Name :</div>
  <div class="abs field" style="left:721px">Password :</div>
  <div class="abs btn-login">LOGIN</div>
  <div class="abs login-meta" style="left:573px">Forget your Password ?</div>
  <div class="abs login-meta" style="left:683px"><span class="check"></span>Remember me</div>
</header>

<nav class="abs nav">
  <a class="active" style="width:153px">HOME</a>
  <a style="width:156px">SERVICES</a>
  <a style="width:138px">LOGIN</a>
  <a style="width:142px">ABOUT</a>
  <a style="width:168px">CONTACT US</a>
</nav>

<section>
  <div class="abs hero" role="img" aria-label="Photo of two business people in suits in front of glass office towers"></div>
  <h1 class="abs hero-title" style="font-weight:400">BK Services</h1>
  <p class="abs hero-text">Company focusses on Sourcing (BK Sourcing, focus on ICT), Metrics (BK Metrics; focus on business case analysis and trends in ICT) and Software (BK software; to be developed later on; mainly tools supporting BK soucing and metrics)</p>
  <div class="abs hero-arrow" style="left:866px"><svg width="8" height="10"><path d="M6 1L2 5l4 4" stroke="#ddd" fill="none"/></svg></div>
  <div class="abs hero-arrow" style="left:888px"><svg width="8" height="10"><path d="M2 1l4 4-4 4" stroke="#ddd" fill="none"/></svg></div>
</section>

<section>
  <div class="abs feature" style="left:183px">
    <div class="feature-icon"><svg width="18" height="18"><path d="M4 16L4 7h5V3l7 6-7 6v-4H8z" fill="#fff"/></svg></div>
    <h3>BK Sourcing</h3>
    <p>Lorem Ipsum is simply dummy text of the printing and typesetting industry. Lorem Ipsum has been the industry's...</p>
  </div>
  <div class="abs feature" style="left:434px">
    <div class="feature-icon"><svg width="20" height="18"><rect x="2" y="10" width="3" height="7" fill="#fff"/><rect x="7" y="7" width="3" height="10" fill="#fff"/><rect x="12" y="9" width="3" height="8" fill="#fff"/><rect x="17" y="4" width="2" height="13" fill="#fff"/><path d="M2 8l5-4 5 3 7-6" stroke="#fff" fill="none"/></svg></div>
    <h3>BK Metrics</h3>
    <p>Lorem Ipsum is simply dummy text of the printing and typesetting industry. Lorem Ipsum has been the industry's...</p>
  </div>
  <div class="abs feature" style="left:682px">
    <div class="feature-icon"><svg width="22" height="16"><rect x="4" y="2" width="14" height="10" fill="none" stroke="#fff" stroke-width="1.5"/><rect x="1" y="12" width="20" height="2" fill="#fff"/></svg></div>
    <h3>BK software</h3>
    <p>Lorem Ipsum is simply dummy text of the printing and typesetting industry. Lorem Ipsum has been the industry's...</p>
  </div>
</section>

<section>
  <h2 class="abs section-title" style="left:181px;top:662px;font-weight:400">Customer Testimonials</h2>
  <svg class="abs" style="left:889px;top:665px" width="20" height="10"><path d="M5 1L2 5l3 4M15 1l3 4-3 4" stroke="#aaa" fill="none"/></svg>
  <div class="abs testi">
    <span class="abs quote" style="left:25px;top:8px">&ldquo;</span>
    <h4>Lorem Ipsum is simply dummy text of the printing and typesetting industry</h4>
    <p>Lorem Ipsum is simply dummy text of the printing and typesetting industry. Lorem Ipsum has been the industry'sLorem Ipsum is simply dummy text of the printing and typesetting industry. Lorem Ipsum has been the industry's...</p>
    <span class="abs quote" style="left:690px;top:64px">&rdquo;</span>
    <div class="author">- Marlon Vesk -</div>
  </div>
</section>

<section>
  <h2 class="abs section-title" style="left:179px;top:833px;font-weight:400">Recent Updates</h2>
  <div class="abs update" style="left:179px">
    <div class="thumb" role="img" aria-label="Photo of business people stacking hands together" style="background:linear-gradient(135deg,#2a2f3a,#d9b59a 50%,#2c3240)"></div>
    <h3>Supporting</h3>
    <p>Lorem Ipsum is simply dummy text of the printing and typesetting industry. Lorem Ipsum has been the industry's...</p>
    <div class="more">Read More</div>
  </div>
  <div class="abs update" style="left:368px">
    <div class="thumb" role="img" aria-label="Photo of a smiling businesswoman" style="background:linear-gradient(90deg,#eef0f2,#c9a58a 55%,#3b2e2a)"></div>
    <h3>Analysis</h3>
    <p>Lorem Ipsum is simply dummy text of the printing and typesetting industry. Lorem Ipsum has been the industry's...</p>
    <div class="more">Read More</div>
  </div>
  <div class="abs update" style="left:557px">
    <div class="thumb" role="img" aria-label="Photo of hands typing on a laptop keyboard" style="background:linear-gradient(160deg,#f3ece6,#e3c6b2 50%,#cfd2d6)"></div>
    <h3>Software</h3>
    <p>Lorem Ipsum is simply dummy text of the printing and typesetting industry. Lorem Ipsum has been the industry's...</p>
    <div class="more">Read More</div>
  </div>
  <div class="abs update" style="left:746px">
    <div class="thumb" role="img" aria-label="Photo of a keyboard with a red help key" style="background:linear-gradient(150deg,#e4e7ea,#c9302c 50%,#eef0f2)"></div>
    <h3>Sourcing</h3>
    <p>Lorem Ipsum is simply dummy text of the printing and typesetting industry. Lorem Ipsum has been the industry's...</p>
    <div class="more">Read More</div>
  </div>
</section>

<footer>
  <div class="abs rule"></div>
  <div class="abs foot-links">HOME<span>|</span>SERVICES<span>|</span>LOGIN<span>|</span>ABOUT<span>|</span>CONTACT US</div>
  <div class="abs copy">© 2013 BK SERVICES. ALL RIGHTS RESERVED</div>
  <div class="abs socials"><i></i><i></i><i></i><i></i><i></i><i></i></div>
</footer>
</body>
</html>
```